Workplace Safety Consultancy Business needs business card design

We need a business card for a new business providing workplace health and safety consulting called 'Worksure Path'. We will be providing small to medium sized businesses assistance with OH&S and HR matters to ensure that their employees and the public are safe in the workplace and that they are meeting their legislative requirements. Would like to see the words 'practical workplace safety solutions' on the card. Personal details on the back. It needs to be clean, smart and professional (no fluff). Would like to see a simple logo if possible as well. Have been looking at orange and black, but open to other ideas.
Updates
Thank you to those to have created designs for us so far! We are really impressed with the impact of the black and orange having now seen it. Would be great if any further designs used those colours. Cheers.

Thank you to everyone that submitted a design. Your work is of the highest quality and we had a hard decision deciding. Sorry if we didn't choose your design, but it just came down to the one that stood out to us personally. Cheers.

Target Market(s)
Small-Medium business owners in Queensland, Australia. Age 25-60 male and female. Initially targeting those in the trade type industries
Industry/Entity Type
Health
Look and feel
Each slider illustrates characteristics of the customer's brand and the style your logo design should communicate.

```html
<!DOCTYPE html>
<html lang="en">
<head>
<meta charset="utf-8">
<title>Worksure Path — Business Card</title>
<link rel="stylesheet" href="https://fonts.googleapis.com/css2?family=Source+Sans+3:wght@400;700&display=swap">
<style>
  :root {
    --page: #ece9e4;
    --card-dark: #231f20;
    --steel-light: #e6e7e9;
    --steel-mid: #a9abae;
    --steel-deep: #6d6f72;
    --orange: #f05a22;
    --white: #ffffff;
  }
  * { box-sizing: border-box; margin: 0; padding: 0; }
  html, body {
    width: 1200px; height: 900px; overflow: hidden;
    background: var(--page);
    font-family: "Source Sans 3", "Myriad Pro", Arial, sans-serif;
  }
  .canvas {
    width: 1200px; height: 900px;
    display: flex; flex-direction: column;
    align-items: center; justify-content: center; gap: 56px;
  }
  .card {
    position: relative;
    width: 620px; height: 380px;
    overflow: hidden;
    box-shadow: 0 6px 18px rgba(0,0,0,0.18);
  }
  .card-bg { position: absolute; inset: 0; width: 100%; height: 100%; }

  /* Front */
  .front-content {
    position: absolute; inset: 0;
    display: flex; flex-direction: column; align-items: center; justify-content: center;
    padding-bottom: 6px;
  }
  .brand-mark {
    width: 46px; height: 46px; border-radius: 50%;
    background: var(--orange);
    margin-bottom: 18px;
  }
  .brand-name {
    color: var(--orange);
    font-weight: 700;
    text-transform: uppercase;
    letter-spacing: 0.5px;
    line-height: 1;
  }
  .front-content .brand-name { font-size: 56px; }
  .tagline {
    color: var(--white);
    font-size: 27px; font-weight: 400;
    margin-top: 8px;
  }

  /* Back */
  .holder {
    position: absolute; left: 62px; top: 92px;
  }
  .holder-name {
    color: var(--orange);
    font-size: 25px; font-weight: 700;
    margin-bottom: 8px;
  }
  .contact-list { list-style: none; }
  .contact-item {
    display: flex; align-items: center; gap: 10px;
    color: var(--white);
    font-size: 18px; line-height: 1.45;
  }
  .contact-icon { width: 16px; height: 16px; flex: none; }
  .back-brand {
    position: absolute; right: 46px; top: 112px;
    display: flex; flex-direction: column; align-items: flex-end; gap: 10px;
  }
  .back-brand .brand-mark { width: 30px; height: 30px; margin: 0 40px 0 0; }
  .back-brand .brand-name { font-size: 32px; }
</style>
</head>
<body>
<main class="canvas">

  <section class="card card-front" aria-label="Card front">
    <svg class="card-bg" viewBox="0 0 620 380" preserveAspectRatio="none" aria-hidden="true">
      <defs>
        <linearGradient id="steel-front" x1="0" y1="0" x2="1" y2="1">
          <stop offset="0" stop-color="var(--steel-light)"/>
          <stop offset="0.5" stop-color="var(--steel-deep)"/>
          <stop offset="1" stop-color="var(--steel-mid)"/>
        </linearGradient>
      </defs>
      <rect width="620" height="380" fill="url(#steel-front)"/>
      <ellipse cx="300" cy="200" rx="400" ry="178" transform="rotate(-9 300 200)" fill="var(--card-dark)"/>
    </svg>
    <div class="front-content">
      <span class="brand-mark" aria-hidden="true"></span>
      <h1 class="brand-name">Worksure Path</h1>
      <p class="tagline">practical workplace safety solutions</p>
    </div>
  </section>

  <section class="card card-back" aria-label="Card back">
    <svg class="card-bg" viewBox="0 0 620 380" preserveAspectRatio="none" aria-hidden="true">
      <defs>
        <linearGradient id="steel-back" x1="0" y1="0" x2="1" y2="1">
          <stop offset="0" stop-color="var(--steel-light)"/>
          <stop offset="0.5" stop-color="var(--steel-deep)"/>
          <stop offset="1" stop-color="var(--steel-mid)"/>
        </linearGradient>
      </defs>
      <rect width="620" height="380" fill="url(#steel-back)"/>
      <ellipse cx="320" cy="180" rx="420" ry="170" transform="rotate(-4 320 180)" fill="var(--card-dark)"/>
    </svg>

    <div class="holder">
      <h2 class="holder-name">Daniel Carver</h2>
      <ul class="contact-list">
        <li class="contact-item">
          <svg class="contact-icon" viewBox="0 0 16 16" aria-hidden="true"><path fill="var(--white)" d="M3.6 1.2l2.2 2.6-1.3 1.8c.8 1.9 2.2 3.3 4.1 4.1l1.8-1.3 2.6 2.2-1.2 2.4C6.2 13 3 9.8 1.2 4.8z"/></svg>
          <span>0400 123 456</span>
        </li>
        <li class="contact-item">
          <svg class="contact-icon" viewBox="0 0 16 16" aria-hidden="true"><rect x="1" y="3" width="14" height="10" fill="none" stroke="var(--white)" stroke-width="1.4"/><path d="M1 3.5l7 5.5 7-5.5" fill="none" stroke="var(--white)" stroke-width="1.4"/></svg>
          <span>daniel@worksurepath.com.au</span>
        </li>
        <li class="contact-item">
          <svg class="contact-icon" viewBox="0 0 16 16" aria-hidden="true"><g fill="none" stroke="var(--white)" stroke-width="1.2"><circle cx="8" cy="8" r="6.5"/><ellipse cx="8" cy="8" rx="2.8" ry="6.5"/><path d="M1.5 8h13M2.6 4.6h10.8M2.6 11.4h10.8"/></g></svg>
          <span>worksurepath.com.au</span>
        </li>
      </ul>
    </div>

    <div class="back-brand">
      <span class="brand-mark" aria-hidden="true"></span>
      <p class="brand-name">Worksure Path</p>
    </div>
  </section>

</main>
</body>
</html>
```